Collateral Materials for Consulting Firm,Bus Card,Stationary, E Sign, PPT Cover+Temp, & Cover Folder
Business Consulting
Professional
Gerald T. Brantley
President
1847 Halvern Court
Charlottesville, Virginia 22987
gbrantley@brantley.net
www.brantley.net
Please use the word mobile rather than cell in all materials
Note this project consists of these 5 items
1. Business Card
2. Stationary
3. Electronic Signature
4. PowerPoint Cover + PowerPopint Template
5. Cover Folder

```html
<!DOCTYPE html>
<html lang="en">
<head>
<meta charset="utf-8">
<title>Brantley Associates LLC – Business Card</title>
<link rel="stylesheet" href="https://fonts.googleapis.com/css2?family=Cinzel:wght@400;600&display=swap">
<style>
  :root {
    --backdrop: #e7e8eb;
    --card-white: #ffffff;
    --card-top-shade: #f1f2f4;
    --brand-blue: #2c5fc4;
    --brand-blue-light: #4a7fe0;
    --brand-blue-deep: #1f4aa6;
    --navy: #1d3b8a;
    --rule-dark: #2a3038;
    --tab-grey: #6f7177;
    --tab-grey-dark: #5b5d63;
    --text-light: #ffffff;
    --text-soft: #dfe6f7;
  }
  * { margin: 0; padding: 0; box-sizing: border-box; }
  html, body {
    width: 1200px; height: 900px; overflow: hidden;
    background: var(--backdrop);
  }
  .canvas {
    position: relative; width: 1200px; height: 900px;
  }
  .business-card {
    position: absolute; left: 100px; top: 164px;
    width: 1000px; height: 572px;
    background: linear-gradient(180deg, var(--card-white) 0%, var(--card-top-shade) 100%);
    box-shadow: 0 14px 40px rgba(0,0,0,0.18);
    overflow: hidden;
    font-family: "Cinzel", "Times New Roman", serif;
  }
  .blue-field {
    position: absolute; left: 0; right: 0; top: 222px; bottom: 0;
    background: linear-gradient(180deg, var(--brand-blue-light) 0%, var(--brand-blue) 45%, var(--brand-blue-deep) 100%);
    border-top: 3px solid var(--rule-dark);
  }
  .brand {
    position: absolute; left: 44px; top: 108px;
    display: flex; align-items: center; gap: 18px;
  }
  .brand-square {
    width: 92px; height: 92px;
    background: var(--navy);
    margin-top: -30px;
  }
  .brand-text { display: flex; flex-direction: column; }
  .brand-name {
    font-size: 40px; font-weight: 400; color: var(--navy);
    letter-spacing: 1px; line-height: 1;
    border-bottom: 2px solid var(--navy);
    padding-bottom: 6px;
  }
  .brand-tagline {
    font-size: 15px; color: var(--navy);
    letter-spacing: 9px; margin-top: 6px;
  }
  .name-tab {
    position: absolute; right: 0; top: 198px;
    width: 440px; height: 86px;
  }
  .name-tab svg { position: absolute; inset: 0; }
  .name-block {
    position: absolute; right: 40px; top: 14px;
    text-align: right; color: var(--text-light);
  }
  .person-name { font-size: 30px; letter-spacing: 1px; line-height: 1.1; }
  .person-title { font-size: 17px; letter-spacing: 1px; margin-top: 4px; color: var(--text-soft); }
  .contact-list {
    position: absolute; left: 34px; top: 330px;
    list-style: none; color: var(--text-light);
    font-size: 20px; letter-spacing: 0.5px;
  }
  .contact-list li {
    display: flex; align-items: center; gap: 10px;
    height: 31px;
  }
  .contact-list li.no-icon { padding-left: 30px; }
  .contact-icon { width: 20px; height: 20px; flex: none; }
  .card-website {
    position: absolute; right: 44px; top: 352px;
    color: var(--text-light); font-size: 26px; letter-spacing: 1px;
  }
</style>
</head>
<body>
<main class="canvas">
  <article class="business-card">
    <div class="blue-field"></div>

    <header class="brand">
      <div class="brand-square"></div>
      <div class="brand-text">
        <span class="brand-name">Brantley Associates LLC</span>
        <span class="brand-tagline">BUSINESS CONSULTING</span>
      </div>
    </header>

    <div class="name-tab">
      <svg width="440" height="86" viewBox="0 0 440 86" aria-hidden="true">
        <polygon points="18,0 440,0 440,86 0,86" fill="var(--tab-grey)"/>
        <polygon points="18,0 440,0 440,4 17,4" fill="var(--tab-grey-dark)"/>
      </svg>
      <div class="name-block">
        <div class="person-name">Gerald T. Brantley</div>
        <div class="person-title">President</div>
      </div>
    </div>

    <ul class="contact-list">
      <li>
        <svg class="contact-icon" viewBox="0 0 20 20" aria-hidden="true">
          <circle cx="10" cy="10" r="10" fill="#fff"/>
          <path d="M10 4.5a3.5 3.5 0 0 0-3.5 3.5c0 2.6 3.5 7 3.5 7s3.5-4.4 3.5-7A3.5 3.5 0 0 0 10 4.5z" fill="var(--brand-blue)"/>
          <circle cx="10" cy="8" r="1.3" fill="#fff"/>
        </svg>
        1847 Halvern Court
      </li>
      <li class="no-icon">Charlottesville, Virginia 22987</li>
      <li>
        <svg class="contact-icon" viewBox="0 0 20 20" aria-hidden="true">
          <circle cx="10" cy="10" r="10" fill="#fff"/>
          <path d="M6.5 5c.5-.4 1.2-.3 1.5.2l1 1.6c.3.5.2 1-.2 1.4l-.6.5c.6 1.3 1.6 2.3 2.9 2.9l.5-.6c.4-.4.9-.5 1.4-.2l1.6 1c.5.3.6 1 .2 1.5l-.7.8c-.6.6-1.5.8-2.3.4C9.2 13.4 6.6 10.8 5.5 8.2c-.4-.8-.2-1.7.4-2.3z" fill="var(--brand-blue)"/>
        </svg>
        434 555 0142
      </li>
      <li>
        <svg class="contact-icon" viewBox="0 0 20 20" aria-hidden="true">
          <circle cx="10" cy="10" r="10" fill="#fff"/>
          <rect x="7" y="4" width="6" height="12" rx="1.2" fill="var(--brand-blue)"/>
          <rect x="8" y="5.5" width="4" height="7.5" fill="#fff"/>
        </svg>
        434 555 0187
      </li>
      <li>
        <svg class="contact-icon" viewBox="0 0 20 20" aria-hidden="true">
          <circle cx="10" cy="10" r="10" fill="#fff"/>
          <rect x="5" y="6.5" width="10" height="7" fill="var(--brand-blue)"/>
          <path d="M5 6.5l5 4 5-4" stroke="#fff" stroke-width="1" fill="none"/>
        </svg>
        gbrantley@brantley.net
      </li>
      <li>
        <svg class="contact-icon" viewBox="0 0 20 20" aria-hidden="true">
          <circle cx="10" cy="10" r="10" fill="#fff"/>
          <circle cx="10" cy="10" r="5" stroke="var(--brand-blue)" stroke-width="1.4" fill="none"/>
          <path d="M5 10h10M10 5c-2 2.8-2 7.2 0 10M10 5c2 2.8 2 7.2 0 10" stroke="var(--brand-blue)" stroke-width="1" fill="none"/>
        </svg>
        www.brantley.net
      </li>
    </ul>

    <div class="card-website">WWW.BRANTLEY.NET</div>
  </article>
</main>
</body>
</html>
```